Flyer für Verkauf von Radondetektoren
Zielgruppe
Ich verkaufe Radondetektoren zur Messung von Radon in Innenräumen. Zielgruppe sind Privatpersonen, Firmen, Genossenschaften und andere Hauseigentümer.
Aufgabenstellung
Ich brauche das Design für meine Messanleitung.
Kreativ - modern - weniger kann mehr sein
Struktur ist wichtigt, es soll also einfach sein zu lesen und zu verstehen, was gemacht werden soll. Können Bulletpoints, Icons mit eingebracht werden.
Wichtig ist auch, dass die beiden Logos 'Luftprüfer.de' und KALVORIX' auf der Messanleitung vorhanden sind. Wobei 'Luftprüfer.de' das Hauptlogo ist.
DIN format dachte ich A4 beidseitig (Text müsste also auf diese Grösse angepasst werden).
Kann natürlich auch Flyer-Format sein oder andere Vorschläge!
Bildmaterial gibt es auf unsere Homepage https://luftprüfer.de und https://luftkollen.se . Diese haben wir bereits gekauft und können verwendet werden. Ich lade sie den bei Bedarf hoch. Es können natürlich auch andere Vorschläge kommen.

```html
<!DOCTYPE html>
<html lang="de">
<head>
<meta charset="utf-8">
<title>Messanleitung – Luftprüfer.de</title>
<link rel="stylesheet" href="https://fonts.googleapis.com/css2?family=Montserrat:wght@600;700&family=Open+Sans:ital,wght@0,400;0,600;0,700;1,400&display=swap">
<style>
:root{
  --canvas:#eeeeee;
  --paper:#f4f4f5;
  --panel:#e3e3e6;
  --red:#d42a2f;
  --ink:#222226;
  --body:#333338;
  --blue:#2f4b9a;
}
*{box-sizing:border-box;margin:0;padding:0}
html,body{width:1200px;height:800px;overflow:hidden;background:var(--canvas)}
body{position:relative;font-family:"Open Sans",sans-serif;color:var(--body)}
.page{position:absolute;top:18px;width:540px;height:764px;background:var(--paper);overflow:hidden;box-shadow:0 6px 18px rgba(0,0,0,.12)}
.page--front{left:40px}
.page--back{left:620px}
.abs{position:absolute}
.panel{position:absolute;background:var(--panel)}
.text{font-size:7.2px;line-height:14.5px;color:var(--body)}
.text em{font-style:italic}
.hl{color:var(--red);font-weight:600}
.red{color:var(--red)}
.logo{display:flex;align-items:center;gap:7px}
.logo__dot{width:18px;height:18px;border-radius:50%;background:var(--red)}
.logo__name{font-size:23px;font-weight:400;color:var(--ink);line-height:1}
.title{font-family:"Montserrat",sans-serif;font-weight:700;color:var(--red);font-size:24px;letter-spacing:.2px}
.subtitle{font-family:"Montserrat",sans-serif;font-weight:700;color:var(--ink);font-size:13.5px;line-height:21.5px}
.scene{position:absolute;background:linear-gradient(180deg,#dfe6ee 0%,#cfd9e6 35%,#a8a0c8 55%,#8fbf6a 80%,#6fa94d 100%)}
.step{position:absolute;display:flex;align-items:flex-start;gap:8px}
.step__icon{width:34px;height:30px;flex:none}
.step__no{font-family:"Montserrat",sans-serif;font-weight:600;color:var(--red);font-size:11px;line-height:12px}
.step__name{font-family:"Montserrat",sans-serif;font-weight:700;color:var(--ink);font-size:8px;line-height:12px;margin-top:1px}
.h-section{font-family:"Open Sans",sans-serif;font-weight:600;font-size:14.5px;color:var(--ink);border-left:2px solid var(--red);padding-left:6px;line-height:17px}
.h-sub{font-size:8px;font-weight:700;color:var(--red);line-height:13px}
.h-sub-row{display:flex;align-items:center;justify-content:space-between;gap:6px}
.bullets{list-style:none}
.bullets li{position:relative;padding-left:14px;font-size:7.2px;line-height:14.5px;margin-bottom:6px}
.bullets li::before{content:"";position:absolute;left:2px;top:4px;width:6px;height:6px;border-radius:50%;background:var(--red)}
.partner{font-size:31px;font-weight:400;color:var(--blue);display:flex;align-items:center;gap:8px;line-height:1}
.partner__dot{width:20px;height:20px;border-radius:50%;background:var(--blue)}
.band{position:absolute;left:0;right:0;bottom:0;height:8px;background:var(--red)}
.footer{position:absolute;left:0;right:0;bottom:0;height:28px;background:var(--red);color:#fff;font-size:7.4px;font-weight:600;display:flex;align-items:center;justify-content:center}
.mail{display:flex;gap:10px;align-items:center}
.mail__addr{font-size:7.6px;font-weight:700;color:var(--red);line-height:14px}
</style>
</head>
<body>

<!-- Vorderseite -->
<section class="page page--front">
  <div class="panel" style="left:0;top:0;width:540px;height:208px"></div>

  <div class="logo abs" style="left:25px;top:36px">
    <div class="logo__dot"></div>
    <div class="logo__name">Luftprüfer.de</div>
  </div>

  <h1 class="title abs" style="left:28px;top:92px">MESSANLEITUNG</h1>
  <p class="subtitle abs" style="left:28px;top:126px">FÜR RADONMESSUNGEN VON<br>INNENRAUMLUFT MIT PASSIVEN<br>RADON DETEKTOREN</p>

  <div class="scene" role="img" aria-label="Illustration: Stadtsilhouette mit Hochhäusern, Wohnhäusern, Bäumen und grünen Hügeln" style="left:249px;top:40px;width:291px;height:168px;clip-path:polygon(8% 12%,100% 0,100% 100%,0 100%,10% 60%)"></div>

  <div class="step" style="left:24px;top:218px">
    <svg class="step__icon" viewBox="0 0 34 30" aria-hidden="true"><circle cx="22" cy="11" r="9" fill="none" stroke="#d42a2f" stroke-width="2"/><circle cx="22" cy="11" r="2.5" fill="#d42a2f"/><path d="M2 27 L12 19 L16 22 L8 29 Z" fill="#d42a2f"/></svg>
    <div><div class="step__no">SCHRITT 1:</div><div class="step__name">REGISTRIERUNG UND ANMELDUNG</div></div>
  </div>
  <p class="text abs" style="left:26px;top:258px;width:500px">Wenn Sie Neukunde sind, legen Sie bitte zunächst ein neues Benutzerkonto auf unserem Online-Portal <span class="hl">https://kunden.kalvorix.de an.</span> Anschließend können Sie die Radondetektoren registrieren. Vermerken Sie den Start der Messung (Datum und Uhrzeit), die Messorte (Raum und Etage) sowie die 9-stellige Seriennummer der Detektoren, die Sie auf der Verpackung oder auf der Unterseite der jeweiligen Detektoren finden.<br><em>Firmenkunden haben die Möglichkeit eine Excel-Datei als Hilfsmittel herunterzuladen, die Sie ausfüllen und dann wieder hochladen.</em></p>

  <div class="step" style="left:24px;top:346px">
    <svg class="step__icon" viewBox="0 0 34 30" aria-hidden="true"><circle cx="22" cy="11" r="9" fill="none" stroke="#d42a2f" stroke-width="2"/><circle cx="22" cy="11" r="2.5" fill="#d42a2f"/><path d="M2 27 L12 19 L16 22 L8 29 Z" fill="#d42a2f"/></svg>
    <div><div class="step__no">SCHRITT 2:</div><div class="step__name">PLATZIERUNG DER DETEKTOREN</div></div>
  </div>
  <p class="text abs" style="left:26px;top:385px;width:500px">Bevor Sie die Detektoren der Verpackung entnehmen, überlegen Sie wo genau Sie die Radondetektoren platzieren wollen. Die Radonmessung beginnt, sobald Sie die radondichten Verpackungen öffnen. Beachten Sie bei der Platzierung zunächst die <span class="hl">Auswahl der Räume</span> und <span class="hl">die Positionierung der Radondetektoren im Raum.</span><br>Für eine zuverlässige Radonmessung empfehlen wir wie folgt vorzugehen:</p>

  <div class="panel" style="left:0;top:452px;width:540px;height:312px"></div>

  <h2 class="h-section abs" style="left:26px;top:466px">Die Auswahl der Räume:</h2>

  <div class="abs" style="left:26px;top:496px;width:224px">
    <div class="h-sub-row">
      <div class="h-sub">Radonmessungen für Einfamilienhäuser:</div>
      <svg width="28" height="26" viewBox="0 0 28 26" aria-hidden="true"><path d="M3 12 L14 3 L25 12 M6 10 V24 H22 V10 M11 24 V17 H17 V24" fill="none" stroke="#d42a2f" stroke-width="1.6"/></svg>
    </div>
    <ul class="bullets" style="margin-top:6px">
      <li>Es sollten mindestens zwei Wohnräume und pro bewohnte Etage mindestens ein Wohnraum gemessen werden. Wählen Sie Räume aus, in denen Sie sich oft aufhalten (z.B. das Wohn- und Schlafzimmer). Vermeiden Sie aber Räume, in denen das Fenster mehrere Stunden am Tag oder in der Nacht geöffnet ist.</li>
      <li>Insofern Sie einen Keller haben, empfehlen wir alle Kellerräume zu messen, da hier meist das größte Risiko einer erhöhten Radonkonzentration erwartet wird.</li>
    </ul>
  </div>

  <div class="abs" style="left:284px;top:463px;width:236px">
    <div class="h-sub-row">
      <div class="h-sub">Radonmessungen für Mehrfamilienhäuser, Wohnungen und Wohnkomplexen:</div>
      <svg width="26" height="30" viewBox="0 0 26 30" aria-hidden="true"><path d="M5 3 H21 V28 H5 Z M9 8 H17 M9 13 H17 M9 18 H17 M11 28 V23 H15 V28" fill="none" stroke="#d42a2f" stroke-width="1.6"/></svg>
    </div>
    <ul class="bullets" style="margin-top:2px">
      <li>Alle Wohnungen mit direktem Bodenkontakt sowie mindestens eine Wohnung pro Etage sollten gemessen werden. Wählen Sie dabei Wohnungen, die an Aufzügen oder Luftschächten liegen.</li>
      <li>In größeren Wohnkomplexen sollten insgesamt mindestens 20% aller Wohnungen in einem Gebäude gemessen werden.</li>
      <li>Es sollten mindestens zwei Wohnräume pro ausgewählte Wohnung gemessen werden. Wählen Sie Räume aus, in denen Sie sich oft aufhalten (z.B. das Wohn- und Schlafzimmer). Vermeiden Sie aber Räume, in denen das Fenster mehrere Stunden am Tag oder in der Nacht geöffnet ist.</li>
      <li>Selbst bei einer Einzimmerwohnung sollten Sie zwei Detektoren aufstellen.</li>
    </ul>
  </div>

  <div class="partner abs" style="left:50px;top:703px"><span class="partner__dot"></span>kalvorix</div>

  <div class="band"></div>
</section>

<!-- Rückseite -->
<section class="page page--back">
  <div class="panel" style="left:0;top:0;width:540px;height:269px"></div>
  <div class="panel" style="left:271px;top:0;width:269px;height:353px"></div>

  <div class="abs" style="left:26px;top:40px;width:230px">
    <div class="h-sub-row">
      <div class="h-sub">Radonmessungen für Arbeitsplätze und öffentliche Gebäude:</div>
      <svg width="30" height="30" viewBox="0 0 30 30" aria-hidden="true"><path d="M3 10 L15 3 L27 10 Z M5 12 H25 M7 14 V25 M12 14 V25 M18 14 V25 M23 14 V25 M3 27 H27" fill="none" stroke="#d42a2f" stroke-width="1.6"/></svg>
    </div>
    <ul class="bullets" style="margin-top:6px">
      <li>Wählen Sie Räume, die regelmäßig mehr als vier Stunden pro Tag genutzt werden.</li>
      <li>Messen Sie alle unterirdischen Räumlichkeiten, da hier meist das größte Risiko einer erhöhten Radonkonzentration erwartet wird.</li>
      <li>Messen Sie alle Räume im Erdgeschoß. Für größere Räumlichkeiten empfehlen wir einen Detektor pro 200 m².</li>
      <li>In den oberen Etagen sollten Sie mit mindestens zwei Detektoren, sowie mindestens einem Detektor pro 200 m² messen.</li>
    </ul>
  </div>

  <h2 class="h-section abs" style="left:301px;top:31px;font-size:14px">Platzierung der Detektoren<br>im Raum:</h2>
  <ul class="bullets abs" style="left:301px;top:78px;width:224px">
    <li>Platzieren Sie die Detektoren in einem Mindestabstand von 20 cm zu Wänden, 50 cm zu Abluftventilen, sowie 1,50 m zu Fenstern, Außentüren, Zuluftsventilen und Heizkörpern.</li>
    <li>Stellen Sie die Detektoren nicht auf dem Boden, an starken Wärmequellen oder Luftströmen auf. Vermeiden Sie auch Räume mit hoher Luftfeuchtigkeit, wie zum Beispiel das Badezimmer.</li>
    <li>Die Detektoren können entweder stehend (auf einem Tisch, im Regal oder einer Schrankwand) oder hängend mitten im Raum (z.B. von einer Lampe) platziert werden.</li>
    <li>Stellen Sie die Detektoren während der gesamten Messdauer nicht um.</li>
    <li>Versuchen Sie nicht das Gehäuse der Detektoren zu öffnen und platzieren Sie diese immer außer Reichweite von Kindern.</li>
  </ul>

  <div class="step" style="left:24px;top:282px">
    <svg class="step__icon" viewBox="0 0 34 30" aria-hidden="true"><circle cx="22" cy="11" r="9" fill="none" stroke="#d42a2f" stroke-width="2"/><circle cx="22" cy="11" r="2.5" fill="#d42a2f"/><path d="M2 27 L12 19 L16 22 L8 29 Z" fill="#d42a2f"/></svg>
    <div><div class="step__no">SCHRITT 3:</div><div class="step__name">RADONMESSUNG</div></div>
  </div>
  <p class="text abs" style="left:26px;top:321px;width:238px">Die Radonmessung beginnt, sobald Sie die radondichten Verpackungen öffnen. <span class="red">Bitte halten Sie die Messdauer wie folgt ein:</span></p>

  <div class="abs" style="left:26px;top:368px;width:240px">
    <div class="h-sub" style="font-size:8.5px;margin-bottom:6px">Kurzzeitmessung:</div>
    <ul class="bullets">
      <li>Mindestmessdauer 10 Tage (bis hin zu 30 Tagen).</li>
      <li>Führen Sie die Messung vorzugsweise in der Heizperiode (1. Oktober – 30. April) durch.</li>
      <li>Kurzzeitmessungen werden oft beim Kauf oder Verkauf von Immobilien genutzt, um ein mögliches Gefährdungspotential abschätzen zu können, oder wenn die Zeit nicht ausreicht, um eine Langzeitmessung durchzuführen.</li>
    </ul>
  </div>
  <div class="abs" style="left:277px;top:368px;width:245px">
    <div class="h-sub" style="font-size:8.5px;margin-bottom:6px">Langzeitmessung:</div>
    <ul class="bullets">
      <li>Mindestmessdauer 3 Monate während der Heizperiode (1. Oktober – 30. April).</li>
      <li>Um einen Jahresmittelwert der Radonkonzentration in Innenräumen ermitteln zu können, halten Sie die Messdauer von 12 Monaten ein.</li>
      <li>Falls Ihr Arbeitsplatz in einem Radon-Vorsorgegebiet liegt und somit der Messpflicht unterliegt, muss die Messdauer von 12 Monaten eingehalten werden.</li>
    </ul>
  </div>

  <div class="step" style="left:24px;top:537px">
    <svg class="step__icon" viewBox="0 0 34 30" aria-hidden="true"><circle cx="22" cy="11" r="9" fill="none" stroke="#d42a2f" stroke-width="2"/><circle cx="22" cy="11" r="2.5" fill="#d42a2f"/><path d="M2 27 L12 19 L16 22 L8 29 Z" fill="#d42a2f"/></svg>
    <div><div class="step__no">SCHRITT 4:</div><div class="step__name">ABSCHLUSS DER RADONMESSUNG MIT ABSCHLIESSENDEM PRÜFBERICHT</div></div>
  </div>
  <p class="text abs" style="left:26px;top:576px;width:500px">Nach Ablauf der Messdauer, loggen Sie sich auf <span class="hl">https://kunden.kalvorix.de</span> in Ihrem Account ein. Vermerken Sie hier das Ende der Messung und senden Sie anschließend alle Radondetektoren ausreichend frankiert in einem Umschlag oder einem Karton zeitnah an unsere Rücksendeadresse:</p>

  <div class="mail abs" style="left:26px;top:626px">
    <svg width="28" height="20" viewBox="0 0 28 20" aria-hidden="true"><rect x="1" y="1" width="26" height="18" fill="none" stroke="#d42a2f" stroke-width="1.8"/><path d="M1 1 L14 11 L27 1 M1 19 L11 9 M27 19 L17 9" fill="none" stroke="#d42a2f" stroke-width="1.8"/></svg>
    <div class="mail__addr">Luftprüfer.de<br>Birkenweg 5 – 27600 Musterfeld – Deutschland</div>
  </div>

  <p class="text abs" style="left:26px;top:663px;width:500px">Sobald die Radondetektoren im Labor von Kalvorix eingetroffen sind, werden diese fachgerecht analysiert und die Ergebnisse der Radonmessung ausgewertet. Ein vollständiger Prüfbericht wird Ihnen innerhalb 36 Stunden nach Erhalt der Detektoren im Labor per E-Mail zugeschickt.</p>

  <div class="footer">Datenschutz (GDPR), Impressum und AGBs: Mehr Information dazu finden Sie unter www.luftprüfer.de</div>
</section>

</body>
</html>
```